New ideas for home page of my website

I am looking for some inspiration for my website www.crafteddownriver.com
Most of the content will stay the same but I will be adding on the following new buttons Annual Expo and Awards
Any ideas on alternative layout act will be great. The most creative idea will get the opportunity to pitch for the whole site design.

Colors

Designer to choose colors to be used in the design.

```html
<!DOCTYPE html>
<html lang="en">
<head>
<meta charset="utf-8">
<title>Crafted Downriver – Home</title>
<link href="https://fonts.googleapis.com/css2?family=Open+Sans:wght@400;600;700&display=swap" rel="stylesheet">
<style>
:root{
  --red:#b3151b;
  --red-dark:#8f0f14;
  --ink:#333;
  --dark:#222;
  --panel:#1f1f1f;
  --grey-band:#e6e6e6;
  --line:#d9d9d9;
  --white:#fff;
}
*{box-sizing:border-box;margin:0;padding:0}
html,body{width:811px;height:1200px;overflow:hidden}
body{position:relative;background:var(--white);font-family:"Open Sans",sans-serif;color:var(--ink)}
.abs{position:absolute}
.brand{left:68px;top:16px;display:flex;align-items:center;gap:12px}
.brand-mark{width:70px;height:70px;border-radius:50%;background:var(--red);border:5px solid #c9c9c9}
.brand-name{font-size:22px;line-height:22px;font-weight:400;color:var(--red);letter-spacing:-.5px}
.btn-dark{background:#3a3a3a;color:#fff;font-size:10px;text-transform:uppercase;padding:4px 7px;border-radius:2px}
.register{left:630px;top:22px}
.login{left:694px;top:22px;background:#777}
.search{left:595px;top:57px;width:146px;height:21px;border:1px solid #ccc;border-radius:2px;font-size:9px;color:#888;padding:4px 9px}
.search svg{position:absolute;right:5px;top:4px}
.nav{left:0;top:99px;width:811px;height:33px;background:var(--red);border-bottom:1px solid var(--red-dark)}
.nav ul{position:absolute;left:67px;top:0;display:flex;list-style:none}
.nav li{font-size:10px;color:#fff;text-transform:uppercase;line-height:33px;padding:0 12.7px}
.nav li.active{background:#2a2a2a;padding:0 12px}
.lang{left:680px;top:105px;width:61px;height:21px;background:#fff;border-radius:2px;font-size:9px;color:#777;padding:4px 0 0 22px}
.lang::before{content:"";position:absolute;left:6px;top:7px;width:11px;height:7px;background:#6b7fa8}
.lang::after{content:"";position:absolute;right:7px;top:9px;border:3px solid transparent;border-top-color:#777}
.hero-band{left:0;top:132px;width:811px;height:308px;background:var(--grey-band)}
.hero-photo{left:67px;top:135px;width:440px;height:301px;background:linear-gradient(135deg,#d8d2c6,#b9ad9a 45%,#6b5f58 75%,#3d3a3c)}
.hero-arrow{width:28px;height:28px;border-radius:50%;background:rgba(255,255,255,.75);top:271px}
.hero-panel{left:507px;top:135px;width:237px;height:301px;background:var(--panel);color:#fff;padding:20px 19px}
.hero-panel h1{font-size:15px;line-height:20px;font-weight:400}
.hero-panel hr{border:0;border-top:1px solid #444;margin:14px 0 17px}
.hero-panel p{font-size:8.8px;line-height:15.6px;color:#ddd}
.read-more{display:inline-block;margin-top:14px;background:#fff;color:var(--ink);font-size:9px;padding:5px 8px;border-radius:2px}
.section-title{font-size:16px;color:var(--red);text-transform:uppercase;font-weight:400}
.next{width:15px;height:14px;border:1px solid #ccc;background:#f7f7f7}
.card{width:141px;height:173px;border:1px solid var(--line);background:#f6f6f6;padding:5px}
.card-img{height:71px}
.card h3{font-size:10px;line-height:14px;font-weight:400;color:var(--red);margin:13px 0 0 5px}
.card p{font-size:8px;line-height:11px;color:#555;margin:11px 0 0 5px}
.logo-tile{background:#fff;display:flex;align-items:center;justify-content:center;gap:6px;font-size:12px;color:var(--red)}
.logo-tile i{width:24px;height:24px;border-radius:50%;background:var(--red);display:block;flex:none}
.side-btn{left:526px;width:218px;height:35px;background:var(--red);color:#fff;font-size:11.5px;text-transform:uppercase;padding:0 0 0 50px;line-height:35px}
.side-btn svg{position:absolute;left:18px;top:9px}
.news-head{left:526px;top:526px;width:218px;height:28px;background:#2f2f2f;color:#fff;font-size:12px;line-height:28px;padding-left:9px}
.news-body{left:526px;top:554px;width:218px;height:116px;background:#e9e9e9}
.field-label{font-size:9px;color:#333}
.field{width:152px;height:23px;background:#fff;border:1px solid #ddd;border-radius:2px}
.submit{left:678px;top:637px;width:53px;height:23px;background:#222;color:#fff;font-size:9.5px;text-align:center;line-height:23px;border-radius:2px}
.ad{left:526px;top:674px;width:218px;height:191px;background:#ededed;padding:12px 9px}
.ad-name{font-size:13px;font-weight:600;color:var(--ink);line-height:18px}
.ad-photo{margin-top:8px;height:112px;background:linear-gradient(120deg,#8a9096,#cfd3d6 50%,#6f7880)}
.ad-text{font-size:7px;line-height:9px;color:#555;text-align:center;margin-top:6px}
.rule{left:67px;width:677px;border-top:1px solid #ddd}
.partners{left:67px;top:900px;width:677px;height:62px;display:flex;justify-content:space-between;align-items:center}
.partner{font-size:13px;font-weight:600;color:var(--ink);display:flex;align-items:center;gap:7px}
.partner i{width:16px;height:16px;display:block;background:#bbb}
.stats-band{left:0;top:980px;width:811px;height:148px;background:#f2f2f2}
.stats{left:0;top:1003px;width:811px;text-align:center;font-size:15.5px;line-height:20px;color:#666}
.clients{left:67px;top:1080px;width:677px;display:flex;justify-content:space-between;align-items:center;font-size:14px;color:#888}
.footer{left:0;top:1128px;width:811px;height:72px;background:var(--dark)}
.footer-links{left:69px;top:1146px;font-size:9px;color:#ccc;word-spacing:1px}
.footer-links span{color:#777;padding:0 5px}
.copyright{left:69px;top:1169px;font-size:9px;color:#ccc}
.social{top:1155px;width:17px;height:17px;border-radius:3px;background:#4a72b4}
</style>
</head>
<body>
<header>
  <div class="abs brand"><span class="brand-mark"></span><span class="brand-name">CRAFTED<br>DOWNRIVER</span></div>
  <div class="abs btn-dark register">Register</div>
  <div class="abs btn-dark login">Log in</div>
  <div class="abs search">Search
    <svg width="12" height="12" viewBox="0 0 12 12"><circle cx="5" cy="5" r="3.8" fill="none" stroke="#777" stroke-width="1.5"/><line x1="8" y1="8" x2="11" y2="11" stroke="#777" stroke-width="1.6"/></svg>
  </div>
</header>
<nav class="abs nav">
  <ul><li class="active">Home</li><li>About us</li><li>News</li><li>Events</li><li>Members</li><li>Council</li><li>Blog</li><li>Contact us</li><li>Partners</li></ul>
</nav>
<div class="abs lang">Eng</div>

<section>
  <div class="abs hero-band"></div>
  <div class="abs hero-photo" role="img" aria-label="Photo of two smiling men in suits at a manufacturing event stand"></div>
  <div class="abs hero-arrow" style="left:78px"><svg width="28" height="28"><polyline points="16,9 11,14 16,19" fill="none" stroke="#888" stroke-width="1.5"/></svg></div>
  <div class="abs hero-arrow" style="left:468px"><svg width="28" height="28"><polyline points="12,9 17,14 12,19" fill="none" stroke="#888" stroke-width="1.5"/></svg></div>
  <article class="abs hero-panel">
    <h1>Crafted Downriver tackles perceived poor image of manufacturing</h1>
    <hr>
    <p>Crafted Downriver has warned that manufacturing’s image as a credible career choice remains poorly perceived based on a recent study.We canvassed our membership of manufacturing and engineering decision makers to develop a Futures Report to assess and forecast industry trends in the next 3 - 5 years.Asked how...</p>
    <span class="read-more">Read full Article</span>
  </article>
</section>

<section>
  <h2 class="abs section-title" style="left:68px;top:455px">Latest News</h2>
  <div class="abs next" style="left:491px;top:459px"><svg width="13" height="12"><polyline points="5,3 8,6 5,9" fill="none" stroke="#555" stroke-width="1.3"/></svg></div>
  <div class="abs card" style="left:68px;top:480px"><div class="card-img logo-tile" style="font-size:20px;color:#1a9ad6">NCW</div><h3>Northgate Circuit Works launch new website</h3><p>By: Northgate Circuit Works Ltd</p></div>
  <div class="abs card" style="left:217px;top:480px"><div class="card-img" role="img" aria-label="Website screenshot with a steel roof photo" style="background:linear-gradient(90deg,#6d7a5e 50%,#f3f3f3 50%);border-top:8px solid var(--red)"></div><h3>Northgate Circuit Works launch new website</h3><p>By: Northgate Circuit Works Ltd</p></div>
  <div class="abs card" style="left:365px;top:480px"><div class="card-img" role="img" aria-label="Photo of industrial gas struts and cylinders" style="background:linear-gradient(90deg,#d6d6d6,#3a3a3a 60%,#bdbdbd)"></div><h3>Northgate Circuit Works launch new website</h3><p>By: Northgate Circuit Works Ltd</p></div>

  <h2 class="abs section-title" style="left:68px;top:667px">Latest Events</h2>
  <div class="abs next" style="left:491px;top:671px"><svg width="13" height="12"><polyline points="5,3 8,6 5,9" fill="none" stroke="#555" stroke-width="1.3"/></svg></div>
  <div class="abs card" style="left:68px;top:692px"><div class="card-img logo-tile"><i></i>Crafted Downriver</div><h3>Northgate Circuit Works launch new website</h3><p>By: Northgate Circuit Works Ltd</p></div>
  <div class="abs card" style="left:217px;top:692px"><div class="card-img" role="img" aria-label="Photo of a modern conference centre building" style="background:linear-gradient(160deg,#9aa6b0,#6d6d6d 55%,#b3b3b3)"></div><h3>Northgate Circuit Works launch new website</h3><p>By: Northgate Circuit Works Ltd</p></div>
  <div class="abs card" style="left:365px;top:692px"><div class="card-img" role="img" aria-label="Photo of a glass building facade and blue sky" style="background:linear-gradient(90deg,#7c8287 50%,#1f5fa8 65%,#2b79c8)"></div><h3>Northgate Circuit Works launch new website</h3><p>By: Northgate Circuit Works Ltd</p></div>
</section>

<aside>
  <div class="abs side-btn" style="top:450px"><svg width="24" height="16"><rect x="1" y="2" width="22" height="12" fill="none" stroke="#fff" stroke-width="1.5"/><line x1="12" y1="2" x2="12" y2="14" stroke="#fff" stroke-width="1.5"/></svg>View latest annual expo</div>
  <div class="abs side-btn" style="top:488px"><svg width="24" height="20"><circle cx="9" cy="6" r="5" fill="none" stroke="#fff" stroke-width="1.5"/><polyline points="6,10 6,18 9,15 12,18 12,10" fill="none" stroke="#fff" stroke-width="1.5"/></svg>View our awards</div>
  <div class="abs news-head">NEWSLETTER SIGNUP</div>
  <div class="abs news-body"></div>
  <span class="abs field-label" style="left:539px;top:575px">Name :</span>
  <div class="abs field" style="left:579px;top:569px"></div>
  <span class="abs field-label" style="left:539px;top:611px">E-mail :</span>
  <div class="abs field" style="left:579px;top:605px"></div>
  <div class="abs submit">SUBMIT</div>
  <div class="abs ad">
    <div class="ad-name">Ferrow Marking Tools Ltd</div>
    <div class="ad-photo" role="img" aria-label="Photo of a dot-peen marking machine stamping a metal part"></div>
    <div class="ad-text">Solutions for marking, identification and<br>traceability needs since 1878<br>E-mail: sales@ferrow-tools.co.uk</div>
  </div>
</aside>

<div class="abs rule" style="top:885px"></div>
<div class="abs partners">
  <span class="partner"><i style="border-radius:50%"></i>Halden Group</span>
  <span class="partner"><i></i>Orvel</span>
  <span class="partner"><i></i>Kestra</span>
  <span class="partner"><i></i>Bramley Lane</span>
  <span class="partner"><i></i>Quarrow Polymers</span>
</div>

<div class="abs stats-band"></div>
<p class="abs stats">MANUFACTURING STATS: 32,000 companies / 600,000 employees<br>The birthplace of the industrial revolution and pioneers in advanced manufacturing</p>
<div class="abs rule" style="top:1062px"></div>
<div class="abs clients"><span>Greenvale</span><span>Lumora</span><span>Netwise</span><span>tally</span><span>Printwell</span><span>Linq</span><span>Corvane</span><span>Artis</span><span>Routa</span></div>

<footer>
  <div class="abs footer"></div>
  <p class="abs footer-links">Home<span>|</span>About Us<span>|</span>Learn more<span>|</span>News<span>|</span>Members<span>|</span>Lobbying<span>|</span>Team<span>|</span>Contact us<span>|</span>Blog<span>|</span>Terms and Conditions</p>
  <p class="abs copyright">Copyright © 2014 Crafted Downriver. &nbsp;All rights reserved.</p>
  <span class="abs social" style="left:706px"></span>
  <span class="abs social" style="left:727px;background:#5aaee0"></span>
</footer>
</body>
</html>
```